New Product/Company Launch Postcard Design

I need a postcard design for a new product launch/new company called Trinvelas. Trinvelas are decorative ring hooks designed to decorate home fixtures for holidays, seasons and special occasions. The rings have hooks for hanging your favorite hanging ornaments, party decorations or fashionable accessories. Trinvelas comes in 3 sizes; small, medium and large with 4 available colors to accommodate most home fixtures. The rings have a split opening for easy attaching or placing on home fixtures, so there are no tools, no glue, the ring is easily attachable. The rings are simply easy to decorate and easy to create ideas.

I would like the postcard to communicate the product use and would like it to drive customers to my website. On this postcard, I am offering $4.99 2-pack special, Introductory offer. I would also like the postcard to direct them to my website to sign up for specials and offers, by doing so, I will give away a free small Trinvela. Please visit my website at www.trinvelasdesigns.com for other creative ideas.

I had someone create the logo, the colors I chose were black, hot pink and yellow. However, if the logo doesn't seem to work on the design, I am open for comments or other ideas.

```html
<!DOCTYPE html>
<html lang="en">
<head>
<meta charset="utf-8">
<title>Trinvelas Launch Postcard</title>
<link rel="stylesheet" href="https://fonts.googleapis.com/css2?family=Yanone+Kaffeesatz:wght@300;400;700&family=Alfa+Slab+One&family=Crimson+Text:wght@700&family=Dosis:wght@600;700&family=Poiret+One&display=swap">
<style>
  :root {
    --backdrop: #e9e6e1;
    --card: #ffffff;
    --ink: #33363f;
    --ink-dark: #2b2d36;
    --pink: #ec1e79;
    --grey: #8c8c8c;
    --dash: #9a9a9a;
    --line: #b9b9b9;
    --photo-warm: #6b5440;
    --photo-light: #b7a48b;
  }
  * { box-sizing: border-box; margin: 0; padding: 0; }
  html, body { width: 1200px; height: 771px; overflow: hidden; }
  body { background: var(--backdrop); position: relative; font-family: "Yanone Kaffeesatz", sans-serif; color: var(--ink); }

  .card { position: absolute; top: 189px; height: 443px; background: var(--card); overflow: hidden; }
  .card--front { left: 24px; width: 574px; }
  .card--back { left: 607px; width: 569px; }

  .abs { position: absolute; }
  .rule-v { position: absolute; width: 2px; background: var(--ink); }

  .ornament { position: absolute; border-radius: 40px; background: linear-gradient(180deg, #e3e3e6, #bfc0c6); opacity: .7; }

  .brand { position: absolute; display: flex; align-items: center; justify-content: center; gap: 8px;
    font-family: "Yanone Kaffeesatz", sans-serif; font-weight: 700; font-size: 26px; letter-spacing: 1px; }
  .brand .dot { width: 10px; height: 10px; }
  .brand--pink { color: var(--pink); }
  .brand--pink .dot { background: var(--pink); }
  .brand--grey { color: var(--grey); }
  .brand--grey .dot { background: var(--grey); }

  .centered { position: absolute; left: 48px; width: 386px; text-align: center; white-space: nowrap; }
  .tagline { font-weight: 300; font-size: 25px; line-height: 1; letter-spacing: .5px; text-transform: uppercase; }
  .tagline em { font-style: normal; color: var(--pink); }
  .headline { font-weight: 400; font-size: 48px; line-height: 1; color: var(--pink); text-transform: uppercase; }
  .offer { font-family: "Poiret One", sans-serif; font-size: 27px; line-height: 1; font-weight: 400; }
  .double-rule { position: absolute; left: 106px; width: 272px; height: 6px; border-top: 2px solid var(--ink); border-bottom: 1px solid var(--ink); }

  .price-banner { position: absolute; left: 128px; width: 226px; height: 36px; top: 484px; }
  .price { position: absolute; left: 0; right: 0; top: 2px; text-align: center; font-family: "Alfa Slab One", serif; font-size: 26px; color: #fff; }
  .sizes { font-family: "Alfa Slab One", serif; font-size: 15px; letter-spacing: .5px; }

  .phone-band { position: absolute; left: 24px; top: 374px; width: 410px; height: 32px; background: var(--pink);
    color: #fff; font-size: 29px; text-align: center; line-height: 32px; letter-spacing: 1px; }
  .web-band { position: absolute; left: 24px; top: 406px; width: 410px; height: 37px; background: var(--ink);
    color: #fff; font-family: "Crimson Text", serif; font-weight: 700; font-size: 15px; letter-spacing: .6px; text-align: center; line-height: 24px; }

  .gallery { position: absolute; left: 422px; top: 0; width: 152px; height: 443px; background: var(--ink-dark); }
  .photo { position: absolute; left: 34px; width: 75px; border: 1px solid #1e1f25; }

  .field-title { position: absolute; font-family: "Dosis", sans-serif; font-weight: 700; font-size: 18px; letter-spacing: 2px; color: var(--ink); }
  .dash { position: absolute; height: 0; border-top: 2px dashed var(--dash); }
  .divider { position: absolute; width: 2px; background: var(--line); }
  .stamp { position: absolute; left: 501px; top: 44px; width: 58px; height: 62px; background: var(--ink-dark); color: #fff;
    font-family: "Dosis", sans-serif; font-size: 8px; font-weight: 600; line-height: 1.05; padding: 14px 0 0 12px; transform: rotate(-8deg); }
  .postmark { position: absolute; left: 440px; top: 66px; width: 86px; height: 40px; border-radius: 20px; background: #d6d6d6; }
  .barcode-label { position: absolute; left: 225px; top: 392px; width: 168px; height: 27px; background: #fff;
    font-family: "Dosis", sans-serif; font-weight: 700; font-size: 19px; letter-spacing: 2.5px; text-align: center; line-height: 27px; color: var(--ink); }
</style>
</head>
<body>

<section class="card card--front" aria-label="Postcard front">
  <div class="rule-v" style="left:17px;top:0;height:443px"></div>
  <div class="rule-v" style="left:22px;top:0;height:443px;width:1px"></div>
  <div class="rule-v" style="left:411px;top:0;height:443px;width:1px"></div>
  <div class="rule-v" style="left:416px;top:0;height:443px"></div>

  <div class="ornament" role="img" aria-label="Scrolling flourish ornament" style="left:12px;top:112px;width:62px;height:218px"></div>
  <div class="ornament" role="img" aria-label="Scrolling flourish ornament" style="left:360px;top:112px;width:62px;height:218px"></div>

  <div class="brand brand--pink" style="left:90px;top:60px;width:256px;height:36px"><span class="dot"></span>Trinvelas</div>

  <p class="centered tagline" style="top:150px;left:24px">A <em>"NEW"</em> SIMPLE HOOK FOR</p>
  <p class="centered tagline" style="top:174px;left:24px">HANGING DECORATIVE ACCESSORIES</p>
  <div class="double-rule" style="left:82px;top:202px"></div>
  <p class="centered headline" style="top:208px;left:24px">EASY TO USE</p>
  <div class="double-rule" style="left:82px;top:252px"></div>
  <p class="centered offer" style="top:264px;left:24px">Special 2 Pack Only For</p>

  <svg class="price-banner" style="left:106px;top:295px" width="226" height="36" viewBox="0 0 226 36">
    <path d="M0 6 H226 L214 18 L226 30 H0 L12 18 Z" fill="var(--pink)" opacity=".35"/>
    <rect x="56" y="0" width="114" height="36" fill="var(--pink)"/>
  </svg>
  <p class="price abs" style="left:106px;width:226px;top:296px;right:auto">$4.99</p>

  <p class="centered sizes" style="top:348px;left:24px">SMALL I MEDIUM I LARGE</p>

  <p class="phone-band">012 3456 7890</p>
  <p class="web-band">www.trinvelasdesigns.com</p>

  <div class="gallery">
    <div class="photo" role="img" aria-label="Lamp on a side table decorated with a ring hook" style="top:32px;height:112px;background:linear-gradient(160deg,#4a3a2c,#b59c7a 55%,#3a2e24)"></div>
    <div class="photo" role="img" aria-label="Decorative vase in a wooden cabinet niche" style="top:154px;height:130px;background:linear-gradient(170deg,#3d2c1f,var(--photo-warm) 50%,#2e2218)"></div>
    <div class="photo" role="img" aria-label="Table lamp with shade beside a stone wall" style="top:294px;height:132px;background:linear-gradient(180deg,#9b8a74,var(--photo-light) 45%,#4d4034)"></div>
  </div>
</section>

<section class="card card--back" aria-label="Postcard back">
  <div class="ornament" role="img" aria-label="Flourish frame ornament" style="left:18px;top:18px;width:222px;height:110px;border-radius:60px;opacity:.45"></div>
  <div class="brand brand--grey" style="left:66px;top:56px;width:130px;height:32px;font-size:22px"><span class="dot"></span>Trinvelas</div>

  <div class="postmark" role="img" aria-label="Postmark wave lines"></div>
  <div class="stamp">Place<br>stamp<br>here</div>

  <p class="field-title" style="left:65px;top:165px">POST OFFICE AREA</p>
  <p class="field-title" style="left:321px;top:165px">RECEPTION ADDRESS</p>

  <div class="divider" style="left:31px;top:181px;height:146px"></div>
  <div class="divider" style="left:259px;top:181px;height:146px"></div>

  <div class="dash" style="left:41px;width:206px;top:193px"></div>
  <div class="dash" style="left:41px;width:206px;top:222px"></div>
  <div class="dash" style="left:41px;width:206px;top:251px"></div>
  <div class="dash" style="left:41px;width:206px;top:280px"></div>
  <div class="dash" style="left:41px;width:206px;top:310px"></div>

  <div class="dash" style="left:286px;width:268px;top:193px"></div>
  <div class="dash" style="left:286px;width:268px;top:222px"></div>
  <div class="dash" style="left:286px;width:268px;top:251px"></div>
  <div class="dash" style="left:286px;width:268px;top:280px"></div>
  <div class="dash" style="left:286px;width:268px;top:310px"></div>

  <p class="barcode-label">BARCODE AREA</p>
</section>

</body>
</html>
```